Beekeeper needs a label for honey jars

Ciao! I'm from Como Italy
I'm a hobbyist beekeeper and I produce honey for myself and my friends.
I've named my apiary "Teo di sole," a play on words between my nickname (Teo, from Matteo) and the Italian expression "Teo di sole," which translates to "a drizzle of honey" in English.
I need to create a label for my honey glass jars (250 gr and 500 gr).
I don't need a label for commercial purposes. I would like to include at least the name “Apicoltura Teo di sole", the type of honey (e.g., wildflower, acacia...) and a space for the production year, to be handwritten each year.
In the design some references to the world of bees.
For reference, attached a label with a style I like
Attached are the images of the selected jars and their measurements
Thanks and good job!

Target Market(s)

beekeeping, honey

Requirements
Nice to have
• I would like an elegant style with clean graphics.
Should not have
• Predominance of black color.

```html
<!DOCTYPE html>
<html lang="it">
<head>
<meta charset="utf-8">
<title>Apicoltura Teo di sole – Etichetta miele</title>
<link href="https://fonts.googleapis.com/css2?family=Roboto+Condensed:wght@400;700&display=swap" rel="stylesheet">
<style>
  :root {
    --bg: #ececec;
    --paper: #ffffff;
    --ink: #4a4a4a;
    --ink-soft: #777777;
    --gold: #e0a040;
    --gold-light: #f2c26a;
    --dash: #a9a9a9;
    --lake: #2d8fc4;
    --comb: #f3f3f3;
  }
  * { box-sizing: border-box; margin: 0; padding: 0; }
  html, body {
    width: 1200px; height: 1174px; overflow: hidden;
    background: var(--bg);
    font-family: "Roboto Condensed", "Arial Narrow", sans-serif;
  }
  .label {
    position: absolute; left: 170px; top: 127px;
    width: 860px; height: 920px;
    background: var(--paper);
    box-shadow: 0 6px 24px rgba(0,0,0,0.08);
  }
  .label__comb {
    position: absolute; inset: 30px;
    background: radial-gradient(ellipse at 45% 55%, var(--comb) 0%, rgba(243,243,243,0) 70%);
  }
  .label__frame { position: absolute; inset: 0; }
  .label__text { position: absolute; left: 0; right: 0; text-align: center; font-weight: 700; line-height: 1; }
  .label__apiary { top: 118px; font-size: 74px; color: var(--ink); }
  .label__name {
    top: 195px; font-size: 132px;
    background: linear-gradient(90deg, var(--gold) 0%, var(--gold-light) 100%);
    -webkit-background-clip: text; background-clip: text; color: transparent;
  }
  .label__bee {
    position: absolute; left: 270px; top: 354px; width: 320px; height: 260px;
    background: radial-gradient(circle, rgba(224,160,64,0.28) 0%, rgba(224,160,64,0.08) 70%, rgba(224,160,64,0) 100%);
  }
  .label__variety { top: 672px; font-size: 98px; color: var(--ink); }
  .label__place { top: 776px; font-size: 44px; font-weight: 400; color: var(--ink-soft); letter-spacing: 30px; padding-left: 30px; }
  .label__lake {
    position: absolute; left: 312px; top: 824px; width: 236px; height: 34px;
    background: linear-gradient(180deg, var(--lake) 0%, #5fb3e0 100%);
    opacity: 0.85; border-radius: 3px;
  }
  .label__field {
    position: absolute; top: 850px; font-size: 30px; color: var(--ink-soft);
    display: flex; align-items: center; gap: 8px; line-height: 1;
  }
  .label__field::before, .label__field--year::after { content: ""; display: block; width: 54px; height: 3px; background: var(--ink-soft); }
  .label__field--year::before { display: none; }
  .label__field--weight { left: 42px; }
  .label__field--year { right: 42px; }
</style>
</head>
<body>
  <section class="label">
    <div class="label__comb" role="img" aria-label="Faint honeycomb pattern in the background"></div>
    <svg class="label__frame" width="860" height="920" viewBox="0 0 860 920" aria-hidden="true">
      <rect x="17" y="17" width="826" height="886" fill="none" stroke="var(--dash)" stroke-width="7" stroke-dasharray="13 10"/>
    </svg>
    <p class="label__text label__apiary">APICOLTURA</p>
    <h1 class="label__text label__name">TEO DI SOLE</h1>
    <div class="label__bee" role="img" aria-label="Golden line illustration of a bee with a honey drop"></div>
    <h2 class="label__text label__variety">MILLEFIORI</h2>
    <p class="label__text label__place">COMO</p>
    <div class="label__lake" role="img" aria-label="Blue wavy lines evoking the lake"></div>
    <span class="label__field label__field--weight">g</span>
    <span class="label__field label__field--year">Anno</span>
  </section>
</body>
</html>
```